Clinician Harbor Collective

I am a financial planner whose client's are physicians and dentists. As physicians, there is very little time for them to do research on numerous aspects of their business and personal lives. I am looking to build a website that is a 1 stop shop for many of the services/resources they may need. It will be my job to screen the resources/advertisers and place competent people/business's that I know and have a track record on. there will ultimately be 10 or 12 ish areas that I would like to provide resources in:
disability insurance
life insurance
retirement planning
student loan advisors
employment contract and business formation attorneys
accountants
real estate agents
physician mortgages
personal loans
malpractice insurance
physician recruiters
maybe 2 other areas which I have yet to figure out.....
I would like each of these options to be able to be clicked on and a page will open up with the 1 or 2 or 3 or 4 people/business's that I have picked to represent these areas. I would like each specific person/business to have a click here to contact me link in which an email goes to the person and I am copied on the initial correspondence between the physician and the mortgage broker.... just so I can see some of the correspondence they will be receiving.
nowhere on the site do I want it to say my name. there will be certain disclosures that are needed and other wording but I think this is a good starting point.
here are links to two websites with the same general concept. please keep in mind that I want my website to be more on the simple side.
http://www.vantorelmedlink.example/index.html
http://bluestethwealth.example/
Industry/Entity Type
Financial

```html
<!DOCTYPE html>
<html lang="en">
<head>
<meta charset="utf-8">
<title>Clinician Harbor Collective – Our Services</title>
<link href="https://fonts.googleapis.com/css2?family=Titillium+Web:wght@400;600&family=Arimo:wght@400;700&display=swap" rel="stylesheet">
<style>
:root{
  --top-strip:#2c2c2c;
  --header:#3b3b3b;
  --brand-red:#d8340f;
  --brand-red-dark:#b32405;
  --brand-sub:#5a1000;
  --nav-text:#dcdcdc;
  --nav-active:#2a2a2a;
  --title-box:#353535;
  --intro-red:#c4311a;
  --heading:#2f2f2f;
  --muted:#9a9a9a;
  --body-text:#8a8a8a;
  --rule:#e2e2e2;
  --btn-bg:#ececec;
  --btn-border:#c9c9c9;
  --footer-bg:#efefef;
  --footer-text:#a6a6a6;
  --footer-head:#6a6a6a;
  --bottom-bar:#3a3a3a;
  --white:#ffffff;
}
*{margin:0;padding:0;box-sizing:border-box}
html,body{width:747px;height:1200px;overflow:hidden;background:var(--white)}
body{position:relative;font-family:"Arimo",Arial,sans-serif;color:var(--body-text)}
.abs{position:absolute}

/* header */
.top-strip{left:0;top:0;width:747px;height:27px;background:var(--top-strip)}
.header-band{left:0;top:27px;width:747px;height:43px;background:var(--header);border-top:1px solid #4a4a4a}
.hero-band{left:0;top:70px;width:747px;height:47px;background:linear-gradient(#dcdcdc,#f6f6f6 70%,#fff)}
.brand{left:111px;top:0;width:209px;height:77px;background:linear-gradient(#e4461a,var(--brand-red-dark));box-shadow:0 3px 6px rgba(0,0,0,.35);text-align:center;color:var(--white)}
.brand-mark{display:block;width:16px;height:16px;margin:9px auto 4px;border-radius:50%;background:var(--white)}
.brand-name{font-family:"Titillium Web",sans-serif;font-weight:400;font-size:15.5px;line-height:18px;letter-spacing:-.3px}
.brand-tag{font-family:"Titillium Web",sans-serif;font-size:5.6px;color:var(--brand-sub);margin-top:4px;letter-spacing:-.1px}
.search-label{left:485px;top:9px;font-size:6.5px;color:#cfcfcf}
.search-input{left:525px;top:5px;width:94px;height:16px;background:var(--white);border:1px solid #999;font-size:5.5px;color:#aaa;padding:4px 5px}
.search-btn{left:618px;top:5px;width:16px;height:16px;background:#555;border:1px solid #999}
.nav{left:379px;top:40px;display:flex;font-family:"Titillium Web",sans-serif;font-size:6.3px;text-transform:uppercase;color:var(--nav-text)}
.nav a{color:inherit;text-decoration:none;height:16px;line-height:16px;padding:0 7px}
.nav a.active{background:var(--nav-active);border:1px solid #4c4c4c;padding:0 7px;color:var(--white)}

/* title */
.page-title{left:112px;top:90px;width:522px;height:49px;background:var(--title-box);box-shadow:0 4px 6px rgba(0,0,0,.25)}
.page-title h1{font-family:"Titillium Web",sans-serif;font-weight:400;font-size:16px;color:var(--white);margin:13px 0 0 21px}
.intro{left:112px;top:151px;width:522px;text-align:center;font-size:5.6px;color:var(--intro-red);white-space:nowrap}
.intro-rule{left:112px;top:168px;width:522px;height:1px;background:var(--rule)}

/* services */
.service{width:150px}
.c1{left:118px}.c2{left:299px}.c3{left:480px}
.r1{top:181px}.r2{top:388px}.r3{top:591px}.r4{top:792px}
.service h2{font-family:"Titillium Web",sans-serif;font-weight:400;font-size:9.6px;color:var(--heading);line-height:12px}
.service .sub{font-size:5.8px;color:#b0b0b0;margin-top:1px}
.service .shadow-rule{height:4px;margin:6px 0 9px;background:radial-gradient(ellipse at 50% 0,rgba(0,0,0,.12),rgba(0,0,0,0) 70%)}
.photo{width:148px;height:78px;border:1px solid #e3e3e3;padding:3px;background:var(--white);box-shadow:0 1px 2px rgba(0,0,0,.08)}
.photo span{display:block;width:100%;height:100%}
.service p{font-size:5.9px;line-height:10.6px;margin-top:12px;width:146px}
.more{display:inline-block;margin-top:6px;height:13px;line-height:11px;padding:0 5px;font-size:5.4px;color:#555;background:var(--btn-bg);border:1px solid var(--btn-border);text-decoration:none}

.p1{background:linear-gradient(#3b78c2,#7fa9d0 55%,#b8c7cc 70%,#d7c8a4)}
.p2{background:linear-gradient(#4d84bd,#6f95c0 65%,#8a5a3c)}
.p3{background:linear-gradient(135deg,#e4e0d6,#bfb29d 60%,#a8977e)}
.p4{background:linear-gradient(135deg,#2e3f6e,#55628a 45%,#7a8a4a)}
.p5{background:linear-gradient(135deg,#f1eee9,#c7b8a4 60%,#4a3b30)}
.p6{background:linear-gradient(135deg,#ececef,#a8a8b0 55%,#34343c)}
.p7{background:linear-gradient(135deg,#23425f,#3c5a78 50%,#9a7660)}
.p8{background:linear-gradient(135deg,#d3e3ee,#8fb6d2 55%,#3f82b4)}
.p9{background:linear-gradient(90deg,#f3eee8,#dcd2c6 55%,#b7c3ad)}
.p10{background:linear-gradient(#f4f4f4,#dcdcdc 60%,#8f9a7f)}
.p11{background:linear-gradient(135deg,#f1f6fb,#9cc0e4 55%,#2f6fb8)}
.p12{background:linear-gradient(135deg,#b8462a,#6a3a6a 50%,#2a5a8a)}

/* footer */
.footer{left:0;top:1040px;width:747px;height:127px;background:var(--footer-bg);border-top:1px solid #dcdcdc}
.to-top{left:602px;top:1025px;width:27px;height:27px;border-radius:50%;background:#5b5b5b;border:2px solid var(--white);box-shadow:0 0 0 1px #9a9a9a}
.foot-glow{left:72px;top:1058px;width:190px;height:40px;border-radius:50%;background:radial-gradient(ellipse,#d6d6d6,rgba(239,239,239,0) 70%)}
.foot-brand{left:111px;top:1038px;width:110px;height:57px;background:var(--white);border:1px solid #e0e0e0;border-top:none;padding:6px 5px}
.foot-brand .name{font-family:"Titillium Web",sans-serif;font-size:11px;color:#a0a0a0;letter-spacing:-.3px;line-height:13px;white-space:nowrap}
.foot-brand .tag{font-size:5.3px;color:#a8a8a8;margin-top:2px;line-height:6.5px}
.social{left:111px;top:1109px;display:flex;align-items:center;font-size:5.8px;color:#555}
.social .icons{display:flex;gap:3px;margin-left:6px}
.social .icons i{display:block;width:8px;height:8px;border-radius:1px;background:#9a9a9a}
.foot-head{font-family:"Titillium Web",sans-serif;font-size:9.6px;color:var(--footer-head)}
.links-head{left:264px;top:1049px}
.contact-head{left:499px;top:1048px}
.links{display:grid;grid-template-columns:85px 85px;column-gap:34px;left:264px;top:1068px}
.links a{display:block;font-size:5.9px;color:var(--footer-text);text-decoration:none;height:16px;line-height:14px;border-bottom:1px solid #e2e2e2}
.contact{left:499px;top:1068px;list-style:none}
.contact li{font-size:5.9px;color:var(--footer-text);height:16px;line-height:14px}
.bottom-bar{left:0;top:1167px;width:747px;height:33px;background:var(--bottom-bar)}
.copy{left:114px;top:1179px;font-size:5.9px;color:#9a9a9a}
.copy b,.credit b{color:#e6e6e6;font-weight:700}
.credit{right:112px;top:1179px;font-size:5.9px;color:#9a9a9a}
</style>
</head>
<body>

<div class="abs top-strip"></div>
<div class="abs header-band"></div>
<div class="abs hero-band"></div>

<header class="abs brand">
  <span class="brand-mark"></span>
  <div class="brand-name">Clinician Harbor Collective</div>
  <div class="brand-tag">FINANCIAL PLANNER WHOSE CLIENTS ARE PHYSICIANS AND DENTISTS</div>
</header>

<div class="abs search-label">Site Search:</div>
<div class="abs search-input">Search</div>
<div class="abs search-btn">
  <svg width="14" height="14" viewBox="0 0 14 14"><circle cx="6" cy="6" r="3" fill="none" stroke="#fff" stroke-width="1.4"/><line x1="8.2" y1="8.2" x2="11" y2="11" stroke="#fff" stroke-width="1.6"/></svg>
</div>

<nav class="abs nav">
  <a class="active" href="#">Home Page</a>
  <a href="#">Blog</a>
  <a href="#">Services</a>
  <a href="#">Follow</a>
  <a href="#">About Us</a>
  <a href="#">Contact</a>
</nav>

<div class="abs page-title"><h1>Our Services</h1></div>
<div class="abs intro">I am a financial planner whose client's are physicians and dentists. As physicians, there is very little time for them to do research on numerous aspects of their business and personal lives</div>
<div class="abs intro-rule"></div>

<main>
  <article class="abs service c1 r1">
    <h2>Disability Insurance</h2><div class="sub">sed congue, dui vel tristique mollis...</div><div class="shadow-rule"></div>
    <div class="photo"><span class="p1" role="img" aria-label="Person in a wheelchair facing the sea with arms open"></span></div>
    <p>Lorem ipsum dolor sit amet, consectetuer adipi-scing elit. Aenean commodo ligula eget dolor. Aenean massa.</p>
    <a class="more" href="#">read more</a>
  </article>
  <article class="abs service c2 r1">
    <h2>Llife Insurance</h2><div class="sub">sed congue, dui vel tristique mollis...</div><div class="shadow-rule"></div>
    <div class="photo"><span class="p2" role="img" aria-label="Hands sheltering a paper family cut-out"></span></div>
    <p>Lorem ipsum dolor sit amet, consectetuer adipi-scing elit. Aenean commodo ligula eget dolor.</p>
    <a class="more" href="#">read more</a>
  </article>
  <article class="abs service c3 r1">
    <h2>Retirement Planning</h2><div class="sub">sed congue, dui vel tristique mollis...</div><div class="shadow-rule"></div>
    <div class="photo"><span class="p3" role="img" aria-label="Retired couple reading together"></span></div>
    <p>Aenean commodo ligula eget dolor. Aenean massa. Cum sociis natoque penatibus et magnis dis parturient montes, nascetur ridiculus mus.</p>
    <a class="more" href="#">read more</a>
  </article>

  <article class="abs service c1 r2">
    <h2>Student Loan Advisors</h2><div class="sub">sed congue, dui vel tristique mollis...</div><div class="shadow-rule"></div>
    <div class="photo"><span class="p4" role="img" aria-label="Graduate in cap and gown holding a diploma"></span></div>
    <p>Lorem ipsum dolor sit amet, consectetuer adipi-scing elit. Aenean commodo ligula eget dolor. Aenean massa.</p>
    <a class="more" href="#">read more</a>
  </article>
  <article class="abs service c2 r2">
    <h2>Employment Contract</h2><div class="sub">sed congue, dui vel tristique mollis...</div><div class="shadow-rule"></div>
    <div class="photo"><span class="p5" role="img" aria-label="Hand signing a contract with a pen"></span></div>
    <p>Lorem ipsum dolor sit amet, consectetuer adipi-scing elit. Aenean commodo ligula eget dolor.</p>
    <a class="more" href="#">read more</a>
  </article>
  <article class="abs service c3 r2">
    <h2>Accountants</h2><div class="sub">sed congue, dui vel tristique mollis...</div><div class="shadow-rule"></div>
    <div class="photo"><span class="p6" role="img" aria-label="Accountants reviewing documents at a desk"></span></div>
    <p>Aenean commodo ligula eget dolor. Aenean massa. Cum sociis natoque penatibus et magnis dis parturient montes, nascetur ridiculus mus.</p>
    <a class="more" href="#">read more</a>
  </article>

  <article class="abs service c1 r3">
    <h2>Real Estate Agents</h2><div class="sub">sed congue, dui vel tristique mollis...</div><div class="shadow-rule"></div>
    <div class="photo"><span class="p7" role="img" aria-label="Agent in a suit holding a model house"></span></div>
    <p>Lorem ipsum dolor sit amet, consectetuer adipi-scing elit. Aenean commodo ligula eget dolor. Aenean massa.</p>
    <a class="more" href="#">read more</a>
  </article>
  <article class="abs service c2 r3">
    <h2>Physician Mortgages</h2><div class="sub">sed congue, dui vel tristique mollis...</div><div class="shadow-rule"></div>
    <div class="photo"><span class="p8" role="img" aria-label="Doctor and nurse reviewing a tablet"></span></div>
    <p>Lorem ipsum dolor sit amet, consectetuer adipi-scing elit. Aenean commodo ligula eget dolor.</p>
    <a class="more" href="#">read more</a>
  </article>
  <article class="abs service c3 r3">
    <h2>Personal Loans</h2><div class="sub">sed congue, dui vel tristique mollis...</div><div class="shadow-rule"></div>
    <div class="photo"><span class="p9" role="img" aria-label="Delighted woman holding a fan of banknotes"></span></div>
    <p>Aenean commodo ligula eget dolor. Aenean massa. Cum sociis natoque penatibus et magnis dis parturient montes, nascetur ridiculus mus.</p>
    <a class="more" href="#">read more</a>
  </article>

  <article class="abs service c1 r4">
    <h2>Malpractice Insurance</h2><div class="sub">sed congue, dui vel tristique mollis...</div><div class="shadow-rule"></div>
    <div class="photo"><span class="p10" role="img" aria-label="Doctor in a white coat holding banknotes with a stethoscope"></span></div>
    <p>Lorem ipsum dolor sit amet, consectetuer adipi-scing elit. Aenean commodo ligula eget dolor. Aenean massa.</p>
    <a class="more" href="#">read more</a>
  </article>
  <article class="abs service c2 r4">
    <h2>Physician Recruiters</h2><div class="sub">sed congue, dui vel tristique mollis...</div><div class="shadow-rule"></div>
    <div class="photo"><span class="p11" role="img" aria-label="Magnifying glass picking one figure out of a crowd"></span></div>
    <p>Lorem ipsum dolor sit amet, consectetuer adipi-scing elit. Aenean commodo ligula eget dolor.</p>
    <a class="more" href="#">read more</a>
  </article>
  <article class="abs service c3 r4">
    <h2>Loreum Ipsum</h2><div class="sub">sed congue, dui vel tristique mollis...</div><div class="shadow-rule"></div>
    <div class="photo"><span class="p12" role="img" aria-label="Pile of colourful crayons"></span></div>
    <p>Aenean commodo ligula eget dolor. Aenean massa. Cum sociis natoque penatibus et magnis dis parturient montes, nascetur ridiculus mus.</p>
    <a class="more" href="#">read more</a>
  </article>
</main>

<footer>
  <div class="abs footer"></div>
  <a class="abs to-top" href="#" aria-label="Back to top">
    <svg width="23" height="23" viewBox="0 0 23 23"><polyline points="7.5,13 11.5,9 15.5,13" fill="none" stroke="#fff" stroke-width="2"/></svg>
  </a>
  <div class="abs foot-glow"></div>
  <div class="abs foot-brand">
    <div class="name">Clinician Harbor</div>
    <div class="tag">FINANCIAL PLANNER WHOSE CLIENTS<br>ARE PHYSICIANS AND DENTISTS</div>
  </div>
  <div class="abs social">Social Network
    <span class="icons"><i></i><i></i><i></i><i></i><i></i><i></i></span>
  </div>

  <div class="abs foot-head links-head">Links</div>
  <nav class="abs links">
    <a href="#">Legal Services</a><a href="#">Insurance Services</a>
    <a href="#">Immigration Services</a><a href="#">Retirement Services</a>
    <a href="#">Real Estate Services</a><a href="#">Accounting Services</a>
    <a href="#">Relocation Services</a><a href="#">Actuarial Services</a>
    <a href="#">Banking Services</a><a href="#">Premier Restaurants</a>
    <a href="#">Financial Advisory Services</a><a href="#">Hospital Recruiters</a>
  </nav>

  <div class="abs foot-head contact-head">Contact</div>
  <ul class="abs contact">
    <li>Phone: 123 456 789</li>
    <li>Fax: 123 456 789</li>
    <li>Site: www.yourdomain.com</li>
    <li>Email: xxxxx@yourmail.com</li>
    <li>Address: Lindel Works, Inc. 4120 N. Carrow St.</li>
  </ul>

  <div class="abs bottom-bar"></div>
  <div class="abs copy">© 2014 Copyright <b>Clinician Harbor Collective</b>. All Rights Reserved</div>
  <div class="abs credit">Design By: <b>Northwind Pixel Studio</b></div>
</footer>

</body>
</html>
```